Web Page for The Brannock Law Firm

The Brannock Law Firm, 7 Quillen Lane, Alma, Ga 31510 is a one lawyer trial firm specializing in sever personal injury, including auto accidents, trucking accidents, severe injuries from defective products. Mr Brannock also has been successfully trying these, commercial and business disputes, criminal cases and high net worth divorce cases for over 28 years. He has tried over 100 cases to a jury verdict.

Douglas is a member of all the trial courts of the State of Georgia, including the Northern, Middle and Southern District Federal Courts, the Georgia Court of Appeals, The Georgia Supreme Court, the 11th Circuit Federal Court of appeals and the United States Supreme Court. Douglas holds the largest verdict in South Georgia history of $150,000,000.00. He is a Member of the Peachvale Legal Standards Council and an active member of the Meridian Courtroom Advocates Guild.

Douglas R. Brannock graduated from Pinewick Valley High School in Alma, Georgia in 1978. He received his BBA in Accounting in 1982 and graduated cum laude from the Halloway Institute College of Law in 1986 with a J.D.

Industry/Entity Type

Lawyer

Number of Pages Required

4 page

Requirements
Must have
• Introduction to firm; separate biography of principal; representative cases; testemonials; blog; method of contact

```html
<!DOCTYPE html>
<html lang="en">
<head>
<meta charset="utf-8">
<title>The Brannock Law Firm</title>
<link href="https://fonts.googleapis.com/css2?family=Libre+Baskerville&family=Open+Sans:wght@400;600&family=Arimo&family=Great+Vibes&display=swap" rel="stylesheet">
<style>
:root{
  --red:#e0513f;
  --red-dark:#c8402f;
  --ink:#1c1c1c;
  --text:#6b6b6b;
  --rule:#d8d8d8;
  --footer:#1b1a1a;
  --footer-text:#8e8e8e;
}
*{margin:0;padding:0;box-sizing:border-box}
html,body{width:895px;height:1200px;overflow:hidden;background:#fff}
body{position:relative;font-family:'Arimo',Arial,sans-serif;color:var(--text)}
.abs{position:absolute}
.top-bar{left:0;top:0;width:895px;height:3px;background:var(--red)}
.brand{left:108px;top:18px;display:flex;align-items:center;gap:8px;font-family:'Libre Baskerville',serif;font-size:10px;color:var(--ink);letter-spacing:.3px}
.brand-dot{width:10px;height:10px;border-radius:50%;background:#d9a13a}
.nav{top:39px;left:397px;display:flex;gap:23px;font-family:'Libre Baskerville',serif;font-size:9.6px;color:#555}
.nav .active{color:var(--red)}
.hero{left:105px;top:90px;width:686px;height:296px;background:linear-gradient(100deg,#d84a3b 0%,#e4604c 55%,#ea7560 100%);box-shadow:0 6px 12px rgba(0,0,0,.25);overflow:hidden}
.hero-photo{position:absolute;right:0;top:0;width:290px;height:296px;background:radial-gradient(ellipse at 55% 45%,#f19a86 0%,#e66c57 55%,rgba(230,96,76,0) 80%)}
.hero-title{position:absolute;left:72px;top:82px;font-family:'Libre Baskerville',serif;font-size:25px;letter-spacing:2px;color:#fff}
.hero-text{position:absolute;left:78px;top:124px;width:260px;font-size:10px;line-height:18px;color:#fff}
.hero-btn{position:absolute;left:79px;top:195px;width:76px;height:29px;background:#1a1a1a;color:#fff;font-size:10px;line-height:29px;text-align:center;border-radius:2px}
.dots{position:absolute;left:614px;top:264px;display:flex;gap:5px}
.dots span{width:9px;height:9px;border-radius:50%;background:#fff}
.dots span:first-child{background:#b8392b}
.heading{font-family:'Libre Baskerville',serif;font-size:15px;color:var(--ink);display:flex;align-items:center;gap:10px;white-space:nowrap}
.heading em{font-style:normal;color:var(--red)}
.heading::after{content:"";flex:1;border-top:3px dotted #e3e3e3;margin-top:2px}
.btn{width:56px;height:27px;background:var(--red);color:#fff;font-size:10px;line-height:27px;text-align:center;box-shadow:0 1px 2px rgba(0,0,0,.2)}
.intro-photo{left:105px;top:465px;width:120px;height:115px;border-radius:50%;background:radial-gradient(circle at 50% 55%,#5a4a48,#1e1a1c);border-left:3px solid var(--red)}
.body-text{font-size:8.6px;line-height:16px;color:var(--text);text-align:justify}
.checklist{left:559px;top:472px;width:231px;list-style:none}
.checklist li{height:22.4px;display:flex;align-items:center;gap:12px;font-size:8.3px;border-bottom:1px dotted var(--rule)}
.checklist li:last-child{border-bottom:none}
.tick{width:11px;height:11px;flex:none}
.blog-photo{left:105px;top:725px;width:190px;height:96px;border:3px solid #fff;outline:1px solid #ddd;background:linear-gradient(180deg,#5a78a8,#7f9cc7 60%,#4e6b97)}
.meta{left:108px;top:830px;width:187px;height:26px;border-bottom:1px solid var(--rule);font-family:'Open Sans',sans-serif;font-size:9px;display:flex;justify-content:space-between}
.meta b{font-weight:600;color:var(--ink)}
.post-title{left:108px;top:866px;font-family:'Open Sans',sans-serif;font-weight:600;font-size:10.5px;color:var(--ink)}
.post-by{left:108px;top:882px;font-family:'Open Sans',sans-serif;font-style:italic;font-size:8px}
.quote{position:relative;padding-left:14px}
.quote::before{content:"\201C";position:absolute;left:0;top:-6px;font-family:'Libre Baskerville',serif;font-size:18px;color:#999}
.sign{font-family:'Great Vibes',cursive;font-size:15px;color:var(--red)}
.role{font-size:8.6px}
.case-thumb{width:76px;height:60px;border:3px solid #fff;outline:1px solid #ddd;background:linear-gradient(135deg,#6d4a32,#2e2620)}
.case-title{font-family:'Open Sans',sans-serif;font-size:10px;color:var(--red)}
.case-text{font-family:'Open Sans',sans-serif;font-size:8.6px;line-height:15.5px;text-align:justify}
.footer{left:0;top:1060px;width:895px;height:140px;background:var(--footer)}
.contact-row{left:128px;top:1087px;display:flex;gap:40px;font-family:'Open Sans',sans-serif;font-size:9px;color:var(--footer-text)}
.contact-row span{display:flex;align-items:center;gap:9px}
.contact-row u{color:#bbb}
.footer-rule{left:0;top:1126px;width:895px;border-top:1px solid #2c2b2b}
.footer-links{left:106px;top:1148px;font-family:'Open Sans',sans-serif;font-size:8.2px;color:var(--footer-text);word-spacing:1px}
.copyright{left:105px;top:1168px;font-family:'Open Sans',sans-serif;font-size:8px;color:var(--footer-text)}
.social{left:654px;top:1147px;display:flex;gap:7px}
.social span{width:26px;height:26px;border-radius:50%;background:#555}
</style>
</head>
<body>
<div class="abs top-bar"></div>

<div class="abs brand"><span class="brand-dot"></span>THE BRANNOCK LAW FIRM</div>
<nav class="abs nav"><span class="active">HOME</span><span>WHO WE ARE</span><span>PRACTICE AREAS</span><span>CONTACT US</span><span>RESOURCES</span></nav>

<section class="abs hero">
  <div class="hero-photo" role="img" aria-label="Portrait of the principal attorney in a suit and bow tie, red tinted"></div>
  <h1 class="hero-title">BRANNOCKLAWFIRM</h1>
  <p class="hero-text">Lorem ipsum dolor sit amet, consectetuer adipiscing elit. Aenean commodo ligula eget dolor. Aenean massa. Cum sociis natoque penatibus et magnis</p>
  <div class="hero-btn">Read More</div>
  <div class="dots"><span></span><span></span><span></span><span></span></div>
</section>

<h2 class="abs heading" style="left:105px;top:428px;width:418px">INTRODUCTION TO <em>FIRM</em></h2>
<div class="abs intro-photo" role="img" aria-label="Group photo of the firm's attorneys and staff"></div>
<p class="abs body-text" style="left:238px;top:475px;width:285px">Founded in 1989, the firm practices in business and general civil litigation, personal injury, real estate transaction and litigation,criminal defense, and family law. We love the practice of law and how it can help to resolve your civil and family disputes, to right the wrongs done by others, to protect your constitutional rights if you happened to be accused of a crime, to seek fair monetary compensation if you are entitled to.</p>
<p class="abs body-text" style="left:105px;top:586px;width:418px">We at The Brannock Law Firm can ensure that you are best represented in courts utilizing the most up-to-date laws, diligent preparation and insightful understanding of your matter.</p>
<div class="abs btn" style="left:105px;top:625px">More</div>

<h2 class="abs heading" style="left:559px;top:428px;width:231px">OUR <em>PRINCIPAL</em></h2>
<ul class="abs checklist">
  <li><svg class="tick" viewBox="0 0 12 12"><circle cx="6" cy="6" r="6" fill="#1c1c1c"/><path d="M3.3 6.2l1.8 1.8 3.6-3.8" stroke="#fff" stroke-width="1.4" fill="none"/></svg>Lorem ipsum dolor sit amet, consectetuer</li>
  <li><svg class="tick" viewBox="0 0 12 12"><circle cx="6" cy="6" r="6" fill="#1c1c1c"/><path d="M3.3 6.2l1.8 1.8 3.6-3.8" stroke="#fff" stroke-width="1.4" fill="none"/></svg>adipiscing elit. Aenean commodo ligula</li>
  <li><svg class="tick" viewBox="0 0 12 12"><circle cx="6" cy="6" r="6" fill="#1c1c1c"/><path d="M3.3 6.2l1.8 1.8 3.6-3.8" stroke="#fff" stroke-width="1.4" fill="none"/></svg>eget dolor. Aenean massa. Cum sociis</li>
  <li><svg class="tick" viewBox="0 0 12 12"><circle cx="6" cy="6" r="6" fill="#1c1c1c"/><path d="M3.3 6.2l1.8 1.8 3.6-3.8" stroke="#fff" stroke-width="1.4" fill="none"/></svg>natoque penatibus et magnis dis parturient</li>
  <li><svg class="tick" viewBox="0 0 12 12"><circle cx="6" cy="6" r="6" fill="#1c1c1c"/><path d="M3.3 6.2l1.8 1.8 3.6-3.8" stroke="#fff" stroke-width="1.4" fill="none"/></svg>montes, nascetur ridiculus mus. Donec</li>
  <li><svg class="tick" viewBox="0 0 12 12"><circle cx="6" cy="6" r="6" fill="#1c1c1c"/><path d="M3.3 6.2l1.8 1.8 3.6-3.8" stroke="#fff" stroke-width="1.4" fill="none"/></svg>quam felis, ultricies nec, pellentesque eu,</li>
</ul>
<div class="abs btn" style="left:559px;top:625px">More</div>

<h2 class="abs heading" style="left:104px;top:685px;width:191px">LATEST <em>&nbsp;BLOG</em></h2>
<div class="abs blog-photo" role="img" aria-label="Photo of the firm's stone entrance sign"></div>
<div class="abs meta"><span>November 28, 2014</span><span>&#9675; <b>1</b></span></div>
<div class="abs post-title">Lorem ipsum dolor sit amet,</div>
<div class="abs post-by">Posted by Mark Dell</div>
<p class="abs body-text" style="left:106px;top:900px;width:189px">Consectetur adipisicing elit, sed do eiusmod tempor incididunt ut labore etdolore magna aliqua. Utenim ad minim veniam. quis nostrud exercitation ullamco laboris nisi ut aliquip ex ea commodo consequat. Duis aute irure.</p>
<div class="abs btn" style="left:105px;top:993px">More</div>

<h2 class="abs heading" style="left:332px;top:685px;width:191px">TESTIMONIALS</h2>
<div class="abs" style="left:332px;top:720px;width:188px">
  <p class="body-text quote">Consectetur adipisicing elit, sed do eiusmod tempor incididunt ut labore etdolore magna aliqua. Utenim ad minim veniam. quis nostrud exercitation ullamco laboris nisi ut aliquip ex ea commodo consequat. Duis aute irure.</p>
  <div class="sign" style="margin-top:4px">- Alan Pierce</div>
  <div class="role">Disignation</div>
</div>
<div class="abs" style="left:332px;top:845px;width:188px;border-top:1px solid var(--rule)"></div>
<div class="abs" style="left:332px;top:861px;width:188px">
  <p class="body-text quote">Consectetur adipisicing elit, sed do eiusmod tempor incididunt ut labore etdolore magna aliqua. Utenim ad minim veniam. quis nostrud exercitation ullamco laboris nisi ut aliquip ex ea commodo consequat. Duis aute irure.</p>
  <div class="sign" style="margin-top:4px">- Alan Pierce</div>
  <div class="role">Disignation</div>
</div>
<div class="abs btn" style="left:332px;top:993px">More</div>

<h2 class="abs heading" style="left:559px;top:685px;width:231px">REPRESENTATIVE <em>CASES</em></h2>
<div class="abs case-thumb" style="left:561px;top:726px" role="img" aria-label="Attorneys standing together in a courtroom"></div>
<div class="abs" style="left:652px;top:722px;width:138px"><div class="case-title">Consectetur adipiscing elit</div><p class="case-text" style="margin-top:3px">Sed do eiusmod tempor incididunt ut labore etdolore magna aliqua. Utenim ad minim veniam.</p></div>
<div class="abs case-thumb" style="left:561px;top:813px" role="img" aria-label="Attorney speaking at a courtroom podium"></div>
<div class="abs" style="left:652px;top:806px;width:138px"><div class="case-title">Consectetur adipiscing elit</div><p class="case-text" style="margin-top:3px">Sed do eiusmod tempor incididunt ut labore etdolore magna aliqua. Utenim ad minim veniam.</p></div>
<div class="abs case-thumb" style="left:561px;top:901px" role="img" aria-label="Graduate holding a certificate in a courtroom"></div>
<div class="abs" style="left:652px;top:894px;width:138px"><div class="case-title">Consectetur adipiscing elit</div><p class="case-text" style="margin-top:3px">Sed do eiusmod tempor incididunt ut labore etdolore magna aliqua. Utenim ad minim veniam.</p></div>
<div class="abs btn" style="left:559px;top:993px">More</div>

<footer class="abs footer"></footer>
<div class="abs contact-row">
  <span><svg width="11" height="10" viewBox="0 0 11 10"><path d="M1 3c2-2.5 7-2.5 9 0l-1.5 1.2-1.5-1H4l-1.5 1z M2.5 5h6l1 4h-8z" fill="#8e8e8e"/></svg>+1 912-555-0148 (Phone)</span>
  <span><svg width="11" height="10" viewBox="0 0 11 10"><rect x="2.5" y="0" width="6" height="3" fill="#8e8e8e"/><rect x="0" y="3.5" width="11" height="4.5" rx="1" fill="#8e8e8e"/><rect x="2.5" y="7" width="6" height="3" fill="#b5b5b5"/></svg>+1 912-555-0149 (Fax)</span>
  <span><svg width="11" height="8" viewBox="0 0 11 8"><rect width="11" height="8" fill="#8e8e8e"/><path d="M0 0l5.5 4.5L11 0" stroke="#1b1a1a" fill="none"/></svg><u>info@brannocklawfirm.com</u></span>
  <span><svg width="8" height="11" viewBox="0 0 8 11"><path d="M4 0a4 4 0 0 1 4 4c0 3-4 7-4 7S0 7 0 4a4 4 0 0 1 4-4z" fill="#8e8e8e"/><circle cx="4" cy="4" r="1.5" fill="#1b1a1a"/></svg>48 Harlow Street, Westbury, Georgia</span>
</div>
<div class="abs footer-rule"></div>
<div class="abs footer-links">HOME &nbsp;|&nbsp; WHO WE ARE &nbsp;|&nbsp; PRACTICE AREAS &nbsp;|&nbsp; CONTACT US &nbsp;|&nbsp; RESOURCE</div>
<div class="abs copyright">COPYRIGHT © CORVANE . ALL RIGHTS RESERVED</div>
<div class="abs social"><span></span><span></span><span></span><span></span></div>
</body>
</html>
```